Adult Toys 1hr Delivery Billboard

We need a digital billboard.
We are
Zinqo.ca
Adult toys 1hr delivery
WE DELIVER FROM from 11am to 3am 7 days a week
we only deliver in Toronto Canada
we use zinqo.ca for marketing and branding but the company name is (Bolt of the Willow Dispatch.com )
Fast safe and discreet
keep a private purchase private
We're ready when you're ready
WE deliver to you home, hotel or favorite coffee shop
please visit our website for any other information you may need

if you want to watch our videos for any inspiration here is our youtube channel

https://www.plavora.com/channel/QXrTbLNE2pWvYhsKk9GmPz4R

it is a digital bill board with only 6 sec impressions
cars will be traveling at 100km when passing the billboard so message must be
to the point with the least amount of words
provocative or fun enough to get peoples attention but being "adult toys" sill must be approved by billboard supplier and city so we may choose a winner based on city approval as well.

our main message is Adult toys 1hr delivery

Ive also sent two billboard photos of one of my competitors that were very successful for them. again please note those are from my main competitor. We really need to top their campaign but if you notice theirs was very short and sweet. THEY DON'T OFFER 1HR DELIVERY. we are the only ones in Canada and are the first in the world.

Target Market(s)

men and women 25 to 45

Industry/Entity Type

Adult

Requirements
Must have
• This must be main message "Adult toys 1hr delivery"
Nice to have
• message must be short
we deliver from 11am to 3am
can we put faster than brindlo ?
bright fun attention getting
Should not have
• should not have the word

sex

```html
<!DOCTYPE html>
<html lang="en">
<head>
<meta charset="UTF-8">
<title>Zinqo.ca — 1HR Adult Toys Delivery Billboard</title>
<link rel="stylesheet" href="https://fonts.googleapis.com/css2?family=Archivo+Black&family=Questrial&family=Didact+Gothic&display=swap">
<style>
  :root {
    --page-bg: #14161b;
    --board-top: #40444b;
    --board-bottom: #2e3238;
    --board-frame: #5a6068;
    --hr-red-light: #d92c40;
    --hr-red-dark: #a3172b;
    --text-white: #eeeeee;
    --toys-yellow: #f3a21f;
    --toys-red: #e5402f;
    --band-yellow: #f1b43a;
    --band-orange: #ec7a2c;
    --band-red: #e4472f;
    --band-text: #2b2a2c;
    --brand-orange: #f08a1e;
  }
  * { margin: 0; padding: 0; box-sizing: border-box; }
  html, body {
    width: 1200px;
    height: 801px;
    overflow: hidden;
    background: var(--page-bg);
  }
  .billboard {
    position: absolute;
    left: 40px;
    top: 160px;
    width: 1120px;
    height: 480px;
    background: linear-gradient(180deg, var(--board-top), var(--board-bottom));
    border: 3px solid var(--board-frame);
    overflow: hidden;
  }
  .brand {
    position: absolute;
    left: 330px;
    top: 40px;
    display: flex;
    align-items: center;
    gap: 8px;
  }
  .brand-dot {
    width: 18px;
    height: 18px;
    border-radius: 50%;
    background: var(--brand-orange);
  }
  .brand-name {
    font-family: "Questrial", sans-serif;
    font-size: 26px;
    line-height: 1;
    color: var(--brand-orange);
  }
  .headline-hr {
    position: absolute;
    left: 250px;
    top: 50px;
    font-family: "Archivo Black", sans-serif;
    font-weight: 400;
    font-size: 200px;
    line-height: 1;
    letter-spacing: -3px;
    background: linear-gradient(180deg, var(--hr-red-light), var(--hr-red-dark));
    -webkit-background-clip: text;
    background-clip: text;
    color: transparent;
  }
  .headline-adult {
    position: absolute;
    left: 690px;
    top: 94px;
    font-family: "Questrial", sans-serif;
    font-size: 80px;
    line-height: 1;
    color: var(--text-white);
  }
  .headline-toys {
    position: absolute;
    left: 690px;
    top: 158px;
    font-family: "Questrial", sans-serif;
    font-size: 80px;
    line-height: 1;
    letter-spacing: 20px;
    background: linear-gradient(90deg, var(--toys-yellow), var(--toys-red));
    -webkit-background-clip: text;
    background-clip: text;
    color: transparent;
  }
  .headline-delivery {
    position: absolute;
    left: 245px;
    top: 235px;
    font-family: "Questrial", sans-serif;
    font-size: 90px;
    line-height: 1;
    letter-spacing: 41px;
    color: var(--text-white);
  }
  .service-band {
    position: absolute;
    left: 0;
    top: 350px;
    width: 100%;
    height: 58px;
    background: linear-gradient(90deg, var(--band-yellow) 0%, var(--band-orange) 55%, var(--band-red) 100%);
  }
  .service-area {
    position: absolute;
    right: 174px;
    top: 50%;
    transform: translateY(-50%);
    font-family: "Didact Gothic", sans-serif;
    font-size: 30px;
    color: var(--band-text);
    white-space: nowrap;
  }
  .service-area strong {
    font-family: "Questrial", sans-serif;
    font-weight: 700;
  }
</style>
</head>
<body>
  <main class="billboard">
    <div class="brand">
      <span class="brand-dot"></span>
      <span class="brand-name">Zinqo.ca</span>
    </div>
    <h1 class="headline-hr">1HR</h1>
    <div class="headline-adult">ADULT</div>
    <div class="headline-toys">TOYS</div>
    <div class="headline-delivery">DELIVERY</div>
    <div class="service-band">
      <p class="service-area">We Only Deliver In <strong>TORONTO CANADA</strong></p>
    </div>
  </main>
</body>
</html>
```